Looking for a label design for a product call KAVA. My business is to sell prepack kava to stores and online.
I need Hawaiian Polynesian theme around tradition.

The label need to have "Nalu Kava" that's the name of the product. Can add "traditional herbal drink"

Can be colorful, the label will be print in a oval shape clear label size 4.25"x3.25" and will be put on a black back ground.

I don't want any white.

Target Market(s)

Polynesian population and tourist

Industry/Entity Type

Business

Requirements
Must have
• Name: Nalu Kava
inscription: Traditional Herbal drink
inscription: 100% Dried Powder Kava Roots
Net Wt: 8oz
Nice to have
• Traditional art design.

```html
<!DOCTYPE html>
<html lang="en">
<head>
<meta charset="utf-8">
<title>Nalu Kava – Oval Label</title>
<link rel="stylesheet" href="https://fonts.googleapis.com/css2?family=Cabin:wght@500;600&display=swap">
<style>
  :root {
    --bg-dark: #2b2b2b;
    --bg-mid: #444444;
    --label-edge: #262626;
    --gold-light: #f3d98f;
    --gold: #d9b461;
    --gold-deep: #b58a3a;
    --ink: #1f1f1f;
    --panel-dark: #1c1c1c;
    --panel-mid: #3a3a3a;
    --cream: #fff38a;
  }
  html, body {
    margin: 0;
    padding: 0;
    width: 1200px;
    height: 1000px;
    overflow: hidden;
    background: var(--bg-dark);
  }
  .canvas {
    position: relative;
    width: 1200px;
    height: 1000px;
    background: linear-gradient(90deg, var(--bg-dark) 0%, var(--bg-mid) 50%, var(--bg-dark) 100%);
  }
  .label { position: absolute; inset: 0; }
  .product-name {
    font-family: "Cabin", "Trebuchet MS", sans-serif;
    font-weight: 600;
    font-size: 82px;
    fill: var(--ink);
    text-anchor: middle;
  }
  .info {
    font-family: "Cabin", "Trebuchet MS", sans-serif;
    fill: var(--cream);
    text-anchor: middle;
    font-weight: 500;
  }
  .tagline { font-size: 35px; }
  .ingredients { font-size: 22px; }
  .net-label { font-size: 24px; }
  .net-weight { font-size: 62px; font-weight: 600; }
</style>
</head>
<body>
<div class="canvas">
  <svg class="label" width="1200" height="1000" viewBox="0 0 1200 1000" xmlns="http://www.w3.org/2000/svg">
    <defs>
      <linearGradient id="goldFill" x1="0" y1="0" x2="1" y2="1">
        <stop offset="0" stop-color="var(--gold-light)"/>
        <stop offset="0.5" stop-color="var(--gold)"/>
        <stop offset="1" stop-color="var(--gold-deep)"/>
      </linearGradient>
      <linearGradient id="panelFill" x1="0" y1="0" x2="1" y2="0">
        <stop offset="0" stop-color="var(--panel-dark)"/>
        <stop offset="0.5" stop-color="var(--panel-mid)"/>
        <stop offset="1" stop-color="var(--panel-dark)"/>
      </linearGradient>
      <linearGradient id="crestFill" x1="0" y1="0" x2="0" y2="1">
        <stop offset="0" stop-color="var(--gold-light)"/>
        <stop offset="1" stop-color="var(--gold-deep)"/>
      </linearGradient>
      <clipPath id="innerOval">
        <ellipse cx="600" cy="512" rx="228" ry="305"/>
      </clipPath>
    </defs>

    <ellipse class="label-edge" cx="600" cy="505" rx="272" ry="355" fill="var(--label-edge)"/>
    <ellipse class="gold-ring" cx="600" cy="510" rx="255" ry="328" fill="url(#goldFill)"/>
    <ellipse class="inner-field" cx="600" cy="512" rx="228" ry="305" fill="url(#goldFill)"/>

    <g clip-path="url(#innerOval)">
      <path class="info-panel" d="M360 580 Q600 560 840 580 L840 830 L360 830 Z" fill="url(#panelFill)"/>
      <path d="M360 580 Q600 560 840 580" fill="none" stroke="var(--cream)" stroke-width="3"/>
    </g>
    <ellipse class="inner-rule" cx="600" cy="512" rx="228" ry="305" fill="none" stroke="var(--cream)" stroke-width="3"/>

    <rect class="crest-art" x="455" y="158" width="290" height="180" rx="30"
          fill="url(#crestFill)" stroke="var(--ink)" stroke-width="4"
          role="img" aria-label="Traditional Polynesian carved crest with scrollwork"/>

    <rect class="divider-ornament" x="562" y="566" width="76" height="18" rx="9"
          fill="var(--gold)" role="img" aria-label="Small decorative flourish"/>

    <text class="product-name" x="600" y="490">Nalu Kava</text>

    <text class="info tagline" x="600" y="638">Traditional Herbal Drink</text>
    <text class="info ingredients" x="600" y="668">100% Dried Powder Kava Roots</text>
    <text class="info net-label" x="600" y="712">Net Wt:</text>
    <text class="info net-weight" x="600" y="768">8oz</text>
  </svg>
</div>
</body>
</html>
```